Tobin Quartz Portal Page . It's guarantee project!

We need a clean and professional modern web application portal page
That includes the Login & Application Selection screen

Also, I need to design both Desktop and Mobile sizes.
We have an example design for our target

The application is Jetty Schedule and related data.
Our client is a bit conservative.

Theme color preferred : #00508B (main) #DF0D83 (secondary)

Target Market(s)

Oil & Fuel & Gasoline

Number of Pages Required

2 page

Font styles to use
Sans Serif

Colors
0054AA
0677BA
7BADD7
CADEEF
E8F1F8
E54698
E96AAD
F1A4CE
F9D9EA
FCEFF6

Requirements
Must have
• Login Page & Main Screen

```html
<!DOCTYPE html>
<html lang="en">
<head>
<meta charset="utf-8">
<title>Jetty Connect Portal</title>
<link href="https://fonts.googleapis.com/css2?family=Inter:wght@400;500;600;700&display=swap" rel="stylesheet">
<style>
:root{
  --page:#F6F7F9;
  --navy:#0F4A93;
  --navy-deep:#0B3F82;
  --blue:#0677BA;
  --link:#0054AA;
  --ink:#1E2430;
  --muted:#7A8290;
  --line:#D5DAE1;
  --white:#FFFFFF;
  --pink-1:#EFA3CC;
  --pink-2:#F9D9EA;
  --pink-3:#FCEFF6;
  --pink-accent:#E54698;
  --nav-dim:#9FB9DD;
}
*{box-sizing:border-box;margin:0;padding:0}
html,body{width:1200px;height:1200px;overflow:hidden}
body{background:var(--page);font-family:"Inter",sans-serif;color:var(--ink);position:relative}
.screen{position:absolute;overflow:hidden;
  background:radial-gradient(ellipse 60% 70% at 42% 48%,#0D4184 0%,#114A97 45%,#1351A3 70%,#0E4790 100%);
  box-shadow:0 6px 18px rgba(20,40,80,.12)}
.abs{position:absolute}
.desk-login{left:43px;top:86px;width:820px;height:461px}
.phone-login{left:932px;top:73px;width:225px;height:487px}
.desk-dash{left:43px;top:653px;width:820px;height:461px}
.phone-dash{left:932px;top:640px;width:225px;height:487px}

.status{left:20px;top:8px;width:193px;display:flex;justify-content:space-between;align-items:center;color:var(--white);font-size:9px;font-weight:600}
.home-bar{left:72px;width:81px;height:2px;border-radius:2px;background:rgba(255,255,255,.35)}

/* login card */
.login-card{background:var(--white);border-radius:4px;width:219px;height:273px}
.phone-login .login-card{left:8px;top:96px;width:209px;height:269px}
.desk-login .login-card{left:300px;top:94px}
.brand{font-size:12.5px;font-weight:600;display:flex;align-items:center;gap:6px}
.brand-dot{width:12px;height:12px;border-radius:50%;background:var(--pink-accent)}
.login-card .brand{left:19px;top:20px}
.field-label{left:19px;font-size:8.5px;font-weight:500}
.field{left:19px;right:19px;height:29px;border:1px solid var(--line);display:flex;align-items:center;padding:0 10px;font-size:8px;color:var(--muted)}
.dots{font-size:10px;letter-spacing:.5px;color:var(--ink);flex:1}
.btn{background:var(--blue);color:var(--white);font-weight:600;display:flex;align-items:center;justify-content:center}
.login-btn{left:19px;right:19px;height:31px;font-size:9.5px}
.help{left:19px;font-size:8px}
.help a{color:var(--link);text-decoration:none}

/* dashboard desktop */
.nav-brand{left:33px;top:12px;color:var(--white);font-size:12.5px;font-weight:500}
.nav-brand .brand-dot{background:var(--white)}
.nav-link{top:15px;font-size:9.5px;color:var(--nav-dim)}
.nav-link.active{color:var(--white);font-weight:600}
.bell{width:14px;height:16px}
.user{right:65px;top:10px;text-align:right;color:var(--white)}
.user .name{font-size:9.5px;font-weight:500}
.user .mail{font-size:6.5px;color:#C7D6EC;margin-top:2px}
.avatar{border-radius:50%;background:linear-gradient(135deg,#C9B5A6,#7D6658);border:2px solid rgba(255,255,255,.8)}
.greeting{left:86px;top:80px;font-size:15px;color:var(--white);font-weight:400}
.greeting b{font-weight:600}
.search{background:var(--white);border-radius:2px;display:flex;align-items:center;justify-content:space-between;padding:0 8px 0 13px;font-size:9.5px;color:var(--muted)}
.hero{border-radius:3px;overflow:hidden;background:linear-gradient(180deg,#555457 0%,#5F5852 40%,#4C463F 70%,#3D3B3A 100%);color:var(--white)}
.hero-date{font-weight:600}
.stat{display:flex;flex-direction:column;justify-content:center;padding-left:14px;color:var(--ink)}
.stat .num{font-weight:700;line-height:1}
.stat.in{background:var(--pink-1)} .stat.out{background:var(--pink-2)} .stat.shift{background:var(--pink-3)}
.app-card{background:var(--white);display:flex;align-items:center;justify-content:center;gap:12px;font-size:9.5px;font-weight:500;letter-spacing:.2px}
.app-card svg.ico{width:30px;height:30px}
</style>
</head>
<body>

<!-- desktop login -->
<section class="screen desk-login">
  <div class="login-card abs">
    <div class="brand abs"><span class="brand-dot"></span>Jetty Connect</div>
    <div class="field-label abs" style="top:58px">Email</div>
    <div class="field abs" style="top:74px">admin@domainname.com</div>
    <div class="field-label abs" style="top:113px">Password</div>
    <div class="field abs" style="top:129px"><span class="dots">●●●●●●●●●●●●●●●</span>
      <svg width="11" height="8" viewBox="0 0 22 14" fill="none" stroke="#9AA1AC" stroke-width="1.6"><path d="M1 7s4-6 10-6 10 6 10 6-4 6-10 6S1 7 1 7z"/><circle cx="11" cy="7" r="2.6"/></svg></div>
    <div class="btn login-btn abs" style="top:176px">Login</div>
    <p class="help abs" style="top:227px">Don’t have an account? <a>Register</a></p>
    <p class="help abs" style="top:245px">Forgot Password? <a>Reset Now</a></p>
  </div>
</section>

<!-- mobile login -->
<section class="screen phone-login">
  <div class="status abs"><span>9:41</span>
    <svg width="38" height="8" viewBox="0 0 38 8" fill="#fff"><rect x="0" y="5" width="2" height="3"/><rect x="3" y="3.5" width="2" height="4.5"/><rect x="6" y="2" width="2" height="6"/><rect x="9" y="0.5" width="2" height="7.5"/><path d="M19 8l-2-2.2a3 3 0 0 1 4 0z M15.5 4.3a5.5 5.5 0 0 1 7 0l-1 1a4 4 0 0 0-5 0z M14 2.8a7.8 7.8 0 0 1 10 0l-.9 1a6.4 6.4 0 0 0-8.2 0z"/><rect x="27" y="1" width="10" height="6" rx="1"/></svg></div>
  <div class="login-card abs">
    <div class="brand abs" style="top:17px"><span class="brand-dot"></span>Jetty Connect</div>
    <div class="field-label abs" style="top:54px">Email</div>
    <div class="field abs" style="top:69px">admin@domainname.com</div>
    <div class="field-label abs" style="top:113px">Password</div>
    <div class="field abs" style="top:128px"><span class="dots">●●●●●●●●●●●●●●●</span>
      <svg width="11" height="8" viewBox="0 0 22 14" fill="none" stroke="#9AA1AC" stroke-width="1.6"><path d="M1 7s4-6 10-6 10 6 10 6-4 6-10 6S1 7 1 7z"/><circle cx="11" cy="7" r="2.6"/></svg></div>
    <div class="btn login-btn abs" style="top:177px">Login</div>
    <p class="help abs" style="top:227px">Don’t have an account? <a>Register</a></p>
    <p class="help abs" style="top:245px">Forgot Password? <a>Reset Now</a></p>
  </div>
  <div class="home-bar abs" style="top:479px"></div>
</section>

<!-- desktop dashboard -->
<section class="screen desk-dash">
  <div class="brand nav-brand abs"><span class="brand-dot"></span>Jetty Connect</div>
  <span class="nav-link active abs" style="left:159px">Home</span>
  <span class="nav-link abs" style="left:206px">Schedules</span>
  <span class="nav-link abs" style="left:272px">Report</span>
  <svg class="bell abs" style="left:619px;top:13px" viewBox="0 0 14 16"><path d="M7 1.5a4 4 0 0 0-4 4v3.5L1.5 11.5h11L11 9V5.5a4 4 0 0 0-4-4z" fill="#fff"/><path d="M5.5 13a1.5 1.5 0 0 0 3 0z" fill="#fff"/><circle cx="11" cy="3.5" r="3" fill="var(--pink-accent)"/></svg>
  <div class="user abs"><div class="name">Tobin Quartz</div><div class="mail">tobin@jettyconnect.com</div></div>
  <div class="avatar abs" role="img" aria-label="User profile photo" style="left:764px;top:9px;width:22px;height:22px"></div>

  <div class="avatar abs" role="img" aria-label="User profile photo" style="left:32px;top:68px;width:44px;height:44px"></div>
  <div class="greeting abs">Good morning, <b>Tobin</b></div>
  <div class="search abs" style="left:417px;top:75px;width:325px;height:29px">Search Scheduled
    <svg width="13" height="13" viewBox="0 0 16 16" fill="none" stroke="#1E2430" stroke-width="1.6"><circle cx="6.5" cy="6.5" r="5"/><path d="M10.5 10.5 15 15"/></svg></div>
  <svg class="abs" style="left:759px;top:80px" width="22" height="19" viewBox="0 0 22 19" fill="none" stroke="#fff" stroke-width="1.3"><path d="M1 3h20M1 9.5h20M1 16h20"/><circle cx="14" cy="3" r="2" fill="#114A97"/><circle cx="7" cy="9.5" r="2" fill="#114A97"/><circle cx="14" cy="16" r="2" fill="#114A97"/></svg>

  <div class="hero abs" role="img" aria-label="Harbour town with marina and hilltop basilica" style="left:33px;top:123px;width:753px;height:240px">
    <div class="hero-date abs" style="left:30px;top:24px;font-size:10.5px">Monday, 5 Aug 2024</div>
    <div class="hero-date abs" style="right:30px;top:24px;font-size:10.5px">08:27 AM</div>
    <div class="abs" style="left:30px;top:125px;font-size:15px"><b>49</b> Schedulled Confirmed</div>
    <div class="stat in abs" style="left:30px;top:161px;width:76px;height:56px"><span class="num" style="font-size:20px">17</span><span style="font-size:9.5px;margin-top:4px">Inbound</span></div>
    <div class="stat out abs" style="left:117px;top:161px;width:76px;height:56px"><span class="num" style="font-size:20px">23</span><span style="font-size:9.5px;margin-top:4px">Outbound</span></div>
    <div class="stat shift abs" style="left:203px;top:161px;width:76px;height:56px"><span class="num" style="font-size:20px">9</span><span style="font-size:9.5px;margin-top:4px">Shifting</span></div>
    <div class="btn abs" style="left:578px;top:187px;width:146px;height:30px;font-size:9.5px">View All Schedules</div>
  </div>

  <div class="app-card abs" style="left:33px;top:382px;width:242px;height:44px">
    <svg class="ico" viewBox="0 0 30 30" fill="none" stroke="#3A4150" stroke-width="1"><rect x="2" y="4" width="22" height="22" rx="1"/><path d="M2 9h22M7 2v4M19 2v4"/><path d="M5 12h3v3H5zM10 12h3v3h-3zM15 12h3v3h-3zM5 17h3v3H5zM10 17h3v3h-3z" fill="#7BADD7" stroke="none"/><circle cx="23" cy="23" r="5" fill="#E96AAD" stroke="#fff"/><path d="M20.8 23l1.6 1.6 2.8-3" stroke="#fff"/></svg>
    JETTY PLANNING
    <svg width="10" height="8" viewBox="0 0 10 8" fill="none" stroke="#1E2430" stroke-width="1.2"><path d="M0 4h9M6 1l3 3-3 3"/></svg>
  </div>
  <div class="app-card abs" style="left:289px;top:382px;width:242px;height:44px">
    <svg class="ico" viewBox="0 0 30 30" fill="none" stroke="#3A4150" stroke-width="1"><rect x="2" y="19" width="8" height="6"/><path d="M10 21h4l2 2v2h-6"/><circle cx="5" cy="26" r="1.4"/><circle cx="13" cy="26" r="1.4"/><path d="M17 25h8a2 2 0 0 0 0-4h-6a2 2 0 0 1 0-4h4" stroke-dasharray="1.5 1.5"/><path d="M25 3a3.5 3.5 0 0 0-3.5 3.5c0 2.6 3.5 6 3.5 6s3.5-3.4 3.5-6A3.5 3.5 0 0 0 25 3z" fill="#E96AAD" stroke="none"/></svg>
    JETTY TRACKING
    <svg width="10" height="8" viewBox="0 0 10 8" fill="none" stroke="#1E2430" stroke-width="1.2"><path d="M0 4h9M6 1l3 3-3 3"/></svg>
  </div>
  <div class="app-card abs" style="left:545px;top:382px;width:242px;height:44px">
    <svg class="ico" viewBox="0 0 30 30" fill="none" stroke="#3A4150" stroke-width="1"><rect x="3" y="2" width="24" height="26" rx="1"/><path d="M3 7h24M7 10h16M7 13h10" stroke="#7BADD7"/><path d="M7 27a8 8 0 0 1 16 0" fill="#F9D9EA"/><path d="M15 27l4-5" stroke="#E54698"/></svg>
    JETTY PERFORMANCE
    <svg width="10" height="8" viewBox="0 0 10 8" fill="none" stroke="#1E2430" stroke-width="1.2"><path d="M0 4h9M6 1l3 3-3 3"/></svg>
  </div>
</section>

<!-- mobile dashboard -->
<section class="screen phone-dash">
  <div class="status abs"><span>9:41</span>
    <svg width="38" height="8" viewBox="0 0 38 8" fill="#fff"><rect x="0" y="5" width="2" height="3"/><rect x="3" y="3.5" width="2" height="4.5"/><rect x="6" y="2" width="2" height="6"/><rect x="9" y="0.5" width="2" height="7.5"/><path d="M19 8l-2-2.2a3 3 0 0 1 4 0z M15.5 4.3a5.5 5.5 0 0 1 7 0l-1 1a4 4 0 0 0-5 0z M14 2.8a7.8 7.8 0 0 1 10 0l-.9 1a6.4 6.4 0 0 0-8.2 0z"/><rect x="27" y="1" width="10" height="6" rx="1"/></svg></div>
  <div class="abs" style="left:10px;top:31px;color:#fff;font-size:9px;font-weight:600">Jetty Connect</div>
  <svg class="abs" style="left:78px;top:33px" width="15" height="10" viewBox="0 0 15 10" stroke="#fff" stroke-width="1.3"><path d="M0 1h15M0 9h15"/></svg>
  <svg class="bell abs" style="left:192px;top:29px" viewBox="0 0 14 16"><path d="M7 1.5a4 4 0 0 0-4 4v3.5L1.5 11.5h11L11 9V5.5a4 4 0 0 0-4-4z" fill="#fff"/><path d="M5.5 13a1.5 1.5 0 0 0 3 0z" fill="#fff"/><circle cx="11" cy="3.5" r="3" fill="var(--pink-accent)"/></svg>
  <div class="search abs" style="left:9px;top:60px;width:173px;height:29px;padding-left:8px">Search Scheduled
    <svg width="13" height="13" viewBox="0 0 16 16" fill="none" stroke="#1E2430" stroke-width="1.6"><circle cx="6.5" cy="6.5" r="5"/><path d="M10.5 10.5 15 15"/></svg></div>
  <svg class="abs" style="left:194px;top:64px" width="20" height="19" viewBox="0 0 22 19" fill="none" stroke="#fff" stroke-width="1.3"><path d="M1 3h20M1 9.5h20M1 16h20"/><circle cx="14" cy="3" r="2" fill="#114A97"/><circle cx="7" cy="9.5" r="2" fill="#114A97"/><circle cx="14" cy="16" r="2" fill="#114A97"/></svg>

  <div class="hero abs" role="img" aria-label="Harbour town with marina and hilltop basilica" style="left:9px;top:95px;width:206px;height:207px">
    <div class="hero-date abs" style="left:6px;top:13px;font-size:11px">Monday, 5 Aug 2024</div>
    <div class="hero-date abs" style="left:6px;top:31px;font-size:8.5px">08:27 AM</div>
    <div class="abs" style="left:6px;top:56px;font-size:11px"><b>49</b> Schedulled Confirmed</div>
    <div class="stat in abs" style="left:12px;top:83px;width:58px;height:39px;padding-left:5px"><span class="num" style="font-size:14px">17</span><span style="font-size:8px;margin-top:3px">Inbound</span></div>
    <div class="stat out abs" style="left:74px;top:83px;width:58px;height:39px;padding-left:5px"><span class="num" style="font-size:14px">23</span><span style="font-size:8px;margin-top:3px">Outbound</span></div>
    <div class="stat shift abs" style="left:137px;top:83px;width:58px;height:39px;padding-left:5px"><span class="num" style="font-size:14px">9</span><span style="font-size:8px;margin-top:3px">Shifting</span></div>
    <div class="btn abs" style="left:30px;top:158px;width:147px;height:31px;font-size:9.5px">View All Schedules</div>
  </div>

  <div class="app-card abs" style="left:10px;top:316px;width:204px;height:44px">
    <svg class="ico" viewBox="0 0 30 30" fill="none" stroke="#3A4150" stroke-width="1"><rect x="2" y="4" width="22" height="22" rx="1"/><path d="M2 9h22M7 2v4M19 2v4"/><path d="M5 12h3v3H5zM10 12h3v3h-3zM15 12h3v3h-3zM5 17h3v3H5zM10 17h3v3h-3z" fill="#7BADD7" stroke="none"/><circle cx="23" cy="23" r="5" fill="#E96AAD" stroke="#fff"/><path d="M20.8 23l1.6 1.6 2.8-3" stroke="#fff"/></svg>
    JETTY PLANNING
    <svg width="10" height="8" viewBox="0 0 10 8" fill="none" stroke="#1E2430" stroke-width="1.2"><path d="M0 4h9M6 1l3 3-3 3"/></svg>
  </div>
  <div class="app-card abs" style="left:10px;top:370px;width:204px;height:44px">
    <svg class="ico" viewBox="0 0 30 30" fill="none" stroke="#3A4150" stroke-width="1"><rect x="2" y="19" width="8" height="6"/><path d="M10 21h4l2 2v2h-6"/><circle cx="5" cy="26" r="1.4"/><circle cx="13" cy="26" r="1.4"/><path d="M17 25h8a2 2 0 0 0 0-4h-6a2 2 0 0 1 0-4h4" stroke-dasharray="1.5 1.5"/><path d="M25 3a3.5 3.5 0 0 0-3.5 3.5c0 2.6 3.5 6 3.5 6s3.5-3.4 3.5-6A3.5 3.5 0 0 0 25 3z" fill="#E96AAD" stroke="none"/></svg>
    JETTY TRACKING
    <svg width="10" height="8" viewBox="0 0 10 8" fill="none" stroke="#1E2430" stroke-width="1.2"><path d="M0 4h9M6 1l3 3-3 3"/></svg>
  </div>
  <div class="app-card abs" style="left:10px;top:424px;width:204px;height:44px">
    <svg class="ico" viewBox="0 0 30 30" fill="none" stroke="#3A4150" stroke-width="1"><rect x="3" y="2" width="24" height="26" rx="1"/><path d="M3 7h24M7 10h16M7 13h10" stroke="#7BADD7"/><path d="M7 27a8 8 0 0 1 16 0" fill="#F9D9EA"/><path d="M15 27l4-5" stroke="#E54698"/></svg>
    PORT PERFORMANCE
    <svg width="10" height="8" viewBox="0 0 10 8" fill="none" stroke="#1E2430" stroke-width="1.2"><path d="M0 4h9M6 1l3 3-3 3"/></svg>
  </div>
  <div class="home-bar abs" style="top:480px"></div>
</section>

</body>
</html>
```